Radiant Harvest Gathering 2021

I am looking to create a flyer for a one day prayer retreat our church is organizing. This flyer will be posted on social media, websites, mobile apps, and will also be printed so it can be mailed to people.

I am looking for something professional, with good use of our logo and band colors (logo colors).

I am counting on the designer's skill, creativity, art and knowledge of media communication to produce a flyer that will effectively and quickly convey the message we are trying to spread.

CONTENT OF THE FLYER:
Event title: Radiant Harvest Gathering
Date: Tuesday July 2nd, 2021
Time: 11:00AM - 7:00PM
Bellmore Hotel, 4817 Wexley Avenue, Portland, Maine 04109 (Room: Tamarind)
Event Key words to highlight what the event is about: Prayer, Fasting, Worship, Prophecy, Revival.
Key phrases:
A one day prayer retreat.
Jesus Chris is Lord

Contact info:
www.quvello.org
Phone: 207 555 0148
Email: contact@brookmeadow.org

```html
<!DOCTYPE html>
<html lang="en">
<head>
<meta charset="utf-8">
<title>Radiant Harvest Gathering 2021</title>
<link rel="stylesheet" href="https://fonts.googleapis.com/css2?family=Montserrat:wght@700;800;900&family=Oswald:wght@400&family=Libre+Baskerville&display=swap">
<style>
  :root {
    --navy: #0b315c;
    --navy-deep: #082a50;
    --orange: #f7941d;
    --white: #ffffff;
    --page: #ffffff;
  }
  * { margin: 0; padding: 0; box-sizing: border-box; }
  html, body { width: 1200px; height: 1200px; overflow: hidden; background: var(--page); }
  .flyer {
    position: absolute; left: 197px; top: 30px;
    width: 806px; height: 1140px;
    background: linear-gradient(180deg, var(--navy) 0%, var(--navy-deep) 100%);
    overflow: hidden;
    font-family: "Montserrat", sans-serif;
    color: var(--white);
  }
  .hero-photo {
    position: absolute; left: 0; top: 0; width: 806px; height: 700px;
    background:
      radial-gradient(ellipse 180px 140px at 360px 460px, rgba(150,150,120,0.55), transparent 70%),
      radial-gradient(ellipse 150px 120px at 140px 330px, rgba(130,90,60,0.6), transparent 70%),
      radial-gradient(ellipse 160px 130px at 360px 620px, rgba(190,140,100,0.55), transparent 70%),
      radial-gradient(ellipse 200px 260px at 640px 350px, rgba(170,180,190,0.55), transparent 70%),
      linear-gradient(180deg, #3f6285 0%, #4d6c86 45%, #2e5274 78%, var(--navy) 100%);
  }
  .brand {
    position: absolute; left: 54px; top: 96px;
    font-family: "Montserrat", sans-serif; font-size: 50px; font-weight: 800;
    letter-spacing: 2px; line-height: 1; color: var(--white);
  }
  .tagline {
    position: absolute; left: 56px; top: 156px;
    font-size: 15px; font-weight: 700; letter-spacing: 2px; line-height: 1;
    color: var(--orange);
  }
  .event-title { position: absolute; left: 0; width: 806px; text-align: center; }
  .event-title__lead {
    top: 636px; font-size: 44px; font-weight: 800; color: var(--orange);
    letter-spacing: 13px; padding-left: 13px; line-height: 1;
  }
  .event-title__main {
    top: 684px; font-size: 86px; font-weight: 900; line-height: 1; letter-spacing: 1px;
  }
  .keywords {
    position: absolute; left: 0; width: 806px; text-align: center;
    font-size: 31px; font-weight: 800; letter-spacing: 6px; line-height: 1;
  }
  .keywords--one { top: 771px; }
  .keywords--two { top: 813px; }
  .date { position: absolute; left: 102px; top: 890px; display: flex; align-items: flex-start; }
  .date__day { font-size: 78px; font-weight: 900; line-height: 1; letter-spacing: -1px; }
  .date__suffix { font-size: 26px; font-weight: 800; margin: 2px 10px 0 4px; }
  .date__month { display: flex; flex-direction: column; }
  .date__month-name { font-size: 50px; font-weight: 900; letter-spacing: 7px; line-height: 1; }
  .date__time { font-size: 16px; font-weight: 800; margin-top: 5px; }
  .divider { position: absolute; left: 449px; top: 897px; width: 1px; height: 62px; background: rgba(255,255,255,0.7); }
  .venue {
    position: absolute; left: 461px; top: 895px;
    font-size: 13px; font-weight: 700; line-height: 23px; font-style: normal;
  }
  .contact-band {
    position: absolute; left: 0; top: 1007px; width: 806px; height: 29px;
    background: var(--orange);
    display: flex; justify-content: center; align-items: center;
    font-family: "Oswald", sans-serif; font-size: 16px; letter-spacing: 0.5px; color: var(--white);
  }
  .contact-band__item { padding: 0 11px; }
  .contact-band__item + .contact-band__item { border-left: 1px solid rgba(255,255,255,0.8); }
  .declaration {
    position: absolute; left: 0; top: 1072px; width: 806px; text-align: center;
    font-family: "Libre Baskerville", serif; font-size: 30px; letter-spacing: 12px; padding-left: 12px;
  }
</style>
</head>
<body>
  <main class="flyer">
    <div class="hero-photo" role="img" aria-label="Photo of a small group kneeling in a circle on a carpet, heads bowed in prayer with hands on shoulders"></div>
    <div class="brand">QUVELLO</div>
    <p class="tagline">A ONE DAY PRAYER RETREAT</p>

    <h1>
      <span class="event-title event-title__lead">RADIANT HARVEST</span>
      <span class="event-title event-title__main">GATHERING</span>
    </h1>

    <p class="keywords keywords--one">PRAYER•FASTING•WORSHIP</p>
    <p class="keywords keywords--two">PROPHECY•REVIVAL</p>

    <div class="date">
      <span class="date__day">02</span>
      <span class="date__suffix">ND</span>
      <span class="date__month">
        <span class="date__month-name">JULY</span>
        <span class="date__time">11:00AM - 7:00PM</span>
      </span>
    </div>
    <div class="divider"></div>
    <address class="venue">
      Bellmore Hotel, 4817<br>
      Wexley Avenue, Portland,<br>
      Maine 04109 (Room: Tamarind)
    </address>

    <div class="contact-band">
      <span class="contact-band__item">WWW.QUVELLO.ORG</span>
      <span class="contact-band__item">PHONE: 207 555 0148</span>
      <span class="contact-band__item">EMAIL: CONTACT@BROOKMEADOW.ORG</span>
    </div>

    <p class="declaration">JESUS CHRIS IS LORD</p>
  </main>
</body>
</html>
```